Business Cards and Stationery
Vellomar Development Company
I need single sided standard sized Business Card [3.5" x 2"]
Not sure. Use something compatible with logo.
Professional
Xxxx Xxxxxxx
President
12345 Xxxxxxxxx Xxxxx
Xxxxxxxxx, Xxxxxxxxxx 12345
xxxxxxxxxxx@xxxxxxxxx.xxx
Contractor's License No. 123456
Not that the information will serve as placeholders until the project is awarded and finalized. Actual information will be provided to create final source files.

```html
<!DOCTYPE html>
<html lang="en">
<head>
<meta charset="utf-8">
<title>Vellomar Development Company – Business Card</title>
<link href="https://fonts.googleapis.com/css2?family=Open+Sans:wght@400;600;700&family=Michroma&display=swap" rel="stylesheet">
<style>
  :root {
    --backdrop: #4a3a2e;
    --card-white: #ffffff;
    --card-grey: #eeeef2;
    --band-light: #8a8fb5;
    --band-mid: #5c6190;
    --band-dark: #30345e;
    --swoosh: #b9bac4;
    --ink: #2a2d4f;
    --ink-soft: #55587a;
    --band-text: #ffffff;
  }
  * { margin: 0; padding: 0; box-sizing: border-box; }
  html, body { width: 1200px; height: 778px; overflow: hidden; }
  body {
    background: var(--backdrop);
    font-family: "Open Sans", Arial, sans-serif;
    position: relative;
  }
  .card {
    position: absolute;
    width: 525px;
    height: 300px;
    border-radius: 22px;
    overflow: hidden;
    background: linear-gradient(180deg, var(--card-white) 0%, var(--card-grey) 100%);
    box-shadow: 0 10px 26px rgba(0,0,0,0.35);
  }
  .card--front { left: 60px; top: 70px; }
  .card--back { left: 615px; top: 400px; }
  .card__wave { position: absolute; left: 0; top: 0; width: 100%; height: 100%; }
  .brand {
    position: absolute;
    display: flex;
    align-items: center;
    gap: 12px;
  }
  .brand__dot {
    width: 46px; height: 46px; border-radius: 50%;
    background: var(--band-dark);
  }
  .brand__name {
    font-family: "Michroma", "Open Sans", sans-serif;
    font-size: 24px;
    color: var(--ink);
    letter-spacing: 1px;
  }
  .card--front .brand { left: 34px; top: 72px; }
  .card--back .brand { left: 40px; top: 112px; }
  .holder {
    position: absolute;
    right: 30px; top: 24px;
    text-align: right;
    color: var(--ink);
    font-family: Georgia, "Times New Roman", serif;
    line-height: 1.45;
  }
  .holder__name { font-size: 15px; }
  .holder__title { font-size: 14px; color: var(--ink-soft); }
  .holder__license { font-size: 12px; color: var(--ink-soft); margin-top: 8px; }
  .contact {
    position: absolute;
    left: 0; right: 0; bottom: 22px;
    display: flex;
    padding: 0 26px;
    gap: 22px;
    color: var(--band-text);
    font-size: 10.5px;
    line-height: 1.7;
  }
  .contact__item { display: flex; align-items: center; gap: 6px; }
  .contact__icon { width: 10px; height: 10px; flex: none; }
  .web {
    position: absolute;
    right: 36px; bottom: 42px;
    color: var(--band-text);
    font-family: Georgia, "Times New Roman", serif;
    font-size: 16px;
    font-weight: bold;
  }
</style>
</head>
<body>

<section class="card card--front" aria-label="Business card front">
  <svg class="card__wave" viewBox="0 0 525 300" preserveAspectRatio="none" aria-hidden="true">
    <defs>
      <linearGradient id="bandFront" x1="0" y1="0" x2="0" y2="1">
        <stop offset="0" stop-color="#8a8fb5"/>
        <stop offset="0.45" stop-color="#5c6190"/>
        <stop offset="1" stop-color="#30345e"/>
      </linearGradient>
    </defs>
    <path d="M0 170 C 140 225, 330 120, 525 150 L525 170 C 330 140, 150 245, 0 192 Z" fill="#b9bac4"/>
    <path d="M0 196 C 150 250, 330 150, 525 175 L525 300 L0 300 Z" fill="url(#bandFront)"/>
  </svg>

  <div class="brand">
    <span class="brand__dot"></span>
    <span class="brand__name">VELLOMAR</span>
  </div>

  <div class="holder">
    <p class="holder__name">Lorem Ipsum Sit Amet</p>
    <p class="holder__title">President</p>
    <p class="holder__license">License No. #123456</p>
  </div>

  <div class="contact">
    <div class="contact__block">
      <p>12345 Street No.1, Suit 6,</p>
      <p>City Name, State - 12345</p>
    </div>
    <div class="contact__block">
      <p class="contact__item">
        <svg class="contact__icon" viewBox="0 0 10 10"><path d="M2 1 L4 1 L5 3 L4 4 Q5 6 6 6 L7 5 L9 6 L9 8 Q8 9 7 9 Q1 8 1 2 Q1 1 2 1 Z" fill="#fff"/></svg>
        (123) 456 7890
      </p>
      <p class="contact__item">
        <svg class="contact__icon" viewBox="0 0 10 10"><rect x="1" y="1" width="8" height="8" rx="1" fill="#fff"/></svg>
        (124) 567 8901
      </p>
    </div>
    <div class="contact__block">
      <p class="contact__item">
        <svg class="contact__icon" viewBox="0 0 10 10"><rect x="0.5" y="2" width="9" height="6" fill="none" stroke="#fff"/><path d="M0.5 2 L5 6 L9.5 2" fill="none" stroke="#fff"/></svg>
        loremipsum@email.com
      </p>
      <p class="contact__item">
        <svg class="contact__icon" viewBox="0 0 10 10"><circle cx="5" cy="5" r="4" fill="none" stroke="#fff"/><path d="M1 5 H9 M5 1 V9" stroke="#fff"/></svg>
        www.vellomar.com
      </p>
    </div>
  </div>
</section>

<section class="card card--back" aria-label="Business card back">
  <svg class="card__wave" viewBox="0 0 525 300" preserveAspectRatio="none" aria-hidden="true">
    <defs>
      <linearGradient id="bandBack" x1="0" y1="0" x2="0" y2="1">
        <stop offset="0" stop-color="#8a8fb5"/>
        <stop offset="0.45" stop-color="#5c6190"/>
        <stop offset="1" stop-color="#30345e"/>
      </linearGradient>
    </defs>
    <path d="M0 175 C 150 235, 330 125, 525 150 L525 172 C 330 145, 160 255, 0 198 Z" fill="#b9bac4"/>
    <path d="M0 202 C 160 262, 330 152, 525 176 L525 300 L0 300 Z" fill="url(#bandBack)"/>
  </svg>

  <div class="brand">
    <span class="brand__dot"></span>
    <span class="brand__name">VELLOMAR</span>
  </div>

  <p class="web">www.vellomar.com</p>
</section>

</body>
</html>
```